One Page Brochure for Metal Recycling Company

We are a scrap metal recycling company and is looking for a one page, one sided brochure A4 size for our upcoming marketing campaign.

This brochure will be mass send to alot of prospective client and we would like it to be professional, but clear, simple and engaging.

We would like to have information on the brochure mainly 1) the type of materials we buy and 2) the service we provide

1) Material
- Scrap Aluminium
- Scrap Stainless Steel
- Scrap Alloy
- Scrap Copper / Brass
- Scrap Iron
- Obselete/Scrap Machinery
- Surplus Material

2) Service
- Prompt & Immediate Payment
- On site weighing
- Free Collection
- Free bin for disposal
- Waste disposal

Etc etc.

Our website is www.tanbokleong.com

Attached our logo and also our previous brochure design for reference.

Target Market(s)

Industrial customer

Industry/Entity Type

It Company

Requirements
Must have
• Our products and our services provide

```html
<!DOCTYPE html>
<html lang="en">
<head>
<meta charset="utf-8">
<title>Tan Bok Leong Recycling – Brochure</title>
<link href="https://fonts.googleapis.com/css2?family=Roboto+Condensed:wght@400;500;700&display=swap" rel="stylesheet">
<style>
  :root{
    --gold:#c9961a;
    --gold-bright:#f5b400;
    --gold-band:#c99a22;
    --gold-footer:#d39a0f;
    --gold-light:#f3dba0;
    --icon-dark:#8a5a0c;
    --slate:#5a5757;
    --text-grey:#626262;
    --rule:#cfcfcf;
    --page:#ffffff;
    --backdrop:#e4e4e4;
  }
  *{margin:0;padding:0;box-sizing:border-box}
  html,body{width:1200px;height:1200px;overflow:hidden}
  body{background:var(--backdrop);font-family:"Roboto Condensed",sans-serif;position:relative}
  .brochure{position:absolute;left:176px;top:0;width:848px;height:1200px;background:var(--page);overflow:hidden}
  .top-rule{position:absolute;left:0;top:0;width:100%;height:6px;background:var(--gold)}
  .hero{position:absolute;left:0;top:6px;width:100%;height:345px;
    background:
      linear-gradient(100deg,rgba(70,100,40,.85) 0%,rgba(90,110,50,.55) 22%,rgba(0,0,0,0) 45%),
      linear-gradient(180deg,#9dbbd8 0%,#c9dbe9 30%,#7d8a88 52%,#5a4b35 78%,#46382a 100%)}
  .hero-title{position:absolute;left:38px;top:168px;font-weight:700;font-size:44px;line-height:44px;color:#fff;text-transform:uppercase;letter-spacing:-.5px}
  .hero-title .accent{color:var(--gold-bright)}
  .brand{position:absolute;right:42px;top:26px;text-align:right}
  .brand-mark{display:block;width:56px;height:56px;border:3px solid var(--gold);margin:0 46px 0 auto}
  .brand-name{display:block;margin-top:28px;font-weight:700;font-size:22px;letter-spacing:2px;color:var(--gold);text-transform:uppercase;line-height:1.1}
  .section-band{position:absolute;left:0;top:351px;width:100%;height:41px;background:var(--gold-band);
    color:#fff;font-weight:700;font-size:25px;text-align:center;line-height:42px;text-transform:uppercase}
  .material{position:absolute;text-align:center;width:220px}
  .material svg{display:block;margin:0 auto}
  .material-label{font-size:16px;font-weight:500;color:var(--text-grey);margin-top:4px;white-space:nowrap}
  .divider{position:absolute;left:39px;top:834px;width:770px;height:1px;background:var(--rule)}
  .service-title{position:absolute;left:0;top:856px;width:100%;text-align:center;font-weight:700;font-size:28px;color:var(--gold);text-transform:uppercase}
  .service{position:absolute;top:915px;width:150px;text-align:center}
  .service-icon{display:block;margin:0 auto}
  .service-label{font-size:15px;font-weight:500;color:var(--text-grey);margin-top:6px;line-height:18px}
  .service-sep{position:absolute;top:910px;width:1px;height:80px;background:var(--rule)}
  .footer-shape{position:absolute;left:0;top:0}
  .contact{position:absolute;top:1118px;color:#fff;font-size:13.5px;line-height:17px;display:flex;gap:7px;align-items:flex-start}
  .contact svg{flex:none;margin-top:1px}
</style>
</head>
<body>
<main class="brochure">
  <svg width="0" height="0" style="position:absolute">
    <defs>
      <radialGradient id="metal" cx="45%" cy="40%" r="70%">
        <stop offset="0" stop-color="#d8dde2"/>
        <stop offset=".6" stop-color="#8d949b"/>
        <stop offset="1" stop-color="#4c5258"/>
      </radialGradient>
      <radialGradient id="copper" cx="40%" cy="40%" r="70%">
        <stop offset="0" stop-color="#d9a27a"/>
        <stop offset=".6" stop-color="#9a6547"/>
        <stop offset="1" stop-color="#6d6f70"/>
      </radialGradient>
      <radialGradient id="machinery" cx="50%" cy="50%" r="70%">
        <stop offset="0" stop-color="#9aa0a5"/>
        <stop offset=".6" stop-color="#4a4f55"/>
        <stop offset="1" stop-color="#2a2d31"/>
      </radialGradient>
      <radialGradient id="surplus" cx="50%" cy="50%" r="70%">
        <stop offset="0" stop-color="#8b9590"/>
        <stop offset=".55" stop-color="#d9d4c8"/>
        <stop offset="1" stop-color="#e6c9c9"/>
      </radialGradient>
      <radialGradient id="badge" cx="40%" cy="35%" r="70%">
        <stop offset="0" stop-color="#fbeccc"/>
        <stop offset=".7" stop-color="#e2b660"/>
        <stop offset="1" stop-color="#c9961a"/>
      </radialGradient>
      <symbol id="ring" viewBox="-100 -100 200 200">
        <circle r="86" fill="none" stroke="#c9961a" stroke-width="9"/>
        <polygon points="-106,-24 -64,-24 -86,2" fill="#c9961a"/>
        <polygon points="106,24 64,24 86,-2" fill="#c9961a"/>
      </symbol>
    </defs>
  </svg>

  <div class="top-rule"></div>
  <div class="hero" role="img" aria-label="Photo of two workers in hard hats at a scrap metal yard with an excavator and a large pile of scrap"></div>
  <h1 class="hero-title">Industry<br>Leader in<br><span class="accent">Metal Recycling</span></h1>
  <div class="brand">
    <span class="brand-mark"></span>
    <span class="brand-name">Tan Bok Leong<br>Recycling</span>
  </div>

  <h2 class="section-band">Type of Materials We Buy</h2>

  <!-- materials row 1 -->
  <div class="material" style="left:48px;top:406px">
    <svg width="180" height="180" viewBox="-100 -100 200 200"><circle r="80" fill="url(#metal)" role="img" aria-label="Photo of baled scrap aluminium"/><use href="#ring" x="-100" y="-100" width="200" height="200"/></svg>
    <div class="material-label">Scrap Aluminium</div>
  </div>
  <div class="material" style="left:330px;top:406px">
    <svg width="180" height="180" viewBox="-100 -100 200 200"><circle r="80" fill="url(#metal)" role="img" aria-label="Photo of baled scrap stainless steel"/><use href="#ring" x="-100" y="-100" width="200" height="200"/></svg>
    <div class="material-label">Scrap Stainless Steel</div>
  </div>
  <div class="material" style="left:586px;top:398px">
    <svg width="180" height="180" viewBox="-100 -100 200 200"><circle r="80" fill="url(#metal)" role="img" aria-label="Photo of baled scrap alloy"/><use href="#ring" x="-100" y="-100" width="200" height="200"/></svg>
    <div class="material-label" style="margin-top:12px">Scrap Alloy</div>
  </div>

  <!-- materials row 2 -->
  <div class="material" style="left:13px;top:622px">
    <svg width="174" height="174" viewBox="-100 -100 200 200"><circle r="80" fill="url(#copper)" role="img" aria-label="Photo of copper wire and brass fittings"/><use href="#ring" x="-100" y="-100" width="200" height="200"/></svg>
    <div class="material-label">Scrap Copper / Brass</div>
  </div>
  <div class="material" style="left:218px;top:622px">
    <svg width="174" height="174" viewBox="-100 -100 200 200"><circle r="80" fill="url(#metal)" role="img" aria-label="Photo of scrap iron parts"/><use href="#ring" x="-100" y="-100" width="200" height="200"/></svg>
    <div class="material-label">Scrap Iron</div>
  </div>
  <div class="material" style="left:425px;top:618px">
    <svg width="174" height="174" viewBox="-100 -100 200 200"><circle r="80" fill="url(#machinery)" role="img" aria-label="Photo of obsolete engine machinery"/><use href="#ring" x="-100" y="-100" width="200" height="200"/></svg>
    <div class="material-label" style="margin-top:8px">Obselete/Scrap Machinery</div>
  </div>
  <div class="material" style="left:626px;top:618px">
    <svg width="174" height="174" viewBox="-100 -100 200 200"><circle r="80" fill="url(#surplus)" role="img" aria-label="Photo of a spool of surplus wire"/><use href="#ring" x="-100" y="-100" width="200" height="200"/></svg>
    <div class="material-label" style="margin-top:8px;font-size:17px">Surplus Material</div>
  </div>

  <div class="divider"></div>
  <h2 class="service-title">Service</h2>

  <div class="service" style="left:29px">
    <svg class="service-icon" width="70" height="70" viewBox="0 0 70 70">
      <circle cx="35" cy="35" r="35" fill="url(#badge)"/>
      <rect x="23" y="15" width="22" height="34" rx="3" fill="none" stroke="var(--icon-dark)" stroke-width="3"/>
      <circle cx="34" cy="30" r="6" fill="none" stroke="var(--icon-dark)" stroke-width="2.5"/>
      <path d="M36 38 L48 38 Q52 38 52 44 L50 56 L38 56 Z" fill="var(--icon-dark)"/>
    </svg>
    <div class="service-label">Prompt &amp; Immediate<br>Payment</div>
  </div>
  <div class="service-sep" style="left:182px"></div>

  <div class="service" style="left:178px">
    <svg class="service-icon" width="70" height="70" viewBox="0 0 70 70">
      <circle cx="35" cy="35" r="35" fill="url(#badge)"/>
      <rect x="16" y="32" width="9" height="20" fill="var(--icon-dark)"/>
      <path d="M28 32 L35 18 Q39 14 40 20 L38 30 L50 30 Q55 31 53 36 L50 50 Q49 53 45 53 L28 53 Z" fill="var(--icon-dark)"/>
    </svg>
    <div class="service-label">Free Collection</div>
  </div>
  <div class="service-sep" style="left:326px"></div>

  <div class="service" style="left:323px">
    <svg class="service-icon" width="70" height="70" viewBox="0 0 70 70">
      <circle cx="35" cy="35" r="35" fill="url(#badge)"/>
      <rect x="18" y="18" width="34" height="5" fill="var(--icon-dark)"/>
      <rect x="30" y="14" width="10" height="4" fill="var(--icon-dark)"/>
      <path d="M21 25 L49 25 L46 54 L24 54 Z" fill="none" stroke="var(--icon-dark)" stroke-width="3"/>
      <path d="M30 30 V49 M35 30 V49 M40 30 V49" stroke="var(--icon-dark)" stroke-width="3"/>
    </svg>
    <div class="service-label">Free bin for disposal</div>
  </div>
  <div class="service-sep" style="left:470px"></div>

  <div class="service" style="left:475px">
    <svg class="service-icon" width="70" height="70" viewBox="0 0 70 70">
      <circle cx="35" cy="35" r="35" fill="url(#badge)"/>
      <circle cx="35" cy="21" r="5" fill="none" stroke="var(--icon-dark)" stroke-width="3"/>
      <path d="M24 26 L46 26 L53 53 L17 53 Z" fill="var(--icon-dark)"/>
      <text x="35" y="46" text-anchor="middle" font-family="Roboto Condensed, sans-serif" font-weight="700" font-size="13" fill="#fff">KG</text>
    </svg>
    <div class="service-label">On site weighing</div>
  </div>
  <div class="service-sep" style="left:629px"></div>

  <div class="service" style="left:625px">
    <svg class="service-icon" width="70" height="70" viewBox="0 0 70 70">
      <circle cx="35" cy="35" r="35" fill="url(#badge)"/>
      <rect x="19" y="29" width="26" height="4" fill="var(--icon-dark)"/>
      <path d="M21 34 L43 34 L40 56 L24 56 Z" fill="var(--icon-dark)"/>
      <path d="M26 37 L38 53 M32 37 L39 46 M38 37 L26 53 M33 53 L25 42" stroke="#f3dba0" stroke-width="1.5"/>
      <path d="M44 24 L52 16 M52 16 L46 16 M52 16 L52 22" stroke="var(--icon-dark)" stroke-width="3" fill="none"/>
    </svg>
    <div class="service-label">Waste disposal</div>
  </div>

  <svg class="footer-shape" width="848" height="1200" viewBox="0 0 848 1200" aria-hidden="true">
    <polygon points="152,1096 818,1048 823,1074 254,1185" fill="var(--slate)"/>
    <polygon points="192,1107 848,1072 848,1200 294,1200" fill="var(--gold-footer)"/>
  </svg>

  <div class="contact" style="left:279px">
    <svg width="15" height="20" viewBox="0 0 15 20"><path d="M7.5 0C3.4 0 0 3.3 0 7.4 0 12.6 7.5 20 7.5 20S15 12.6 15 7.4C15 3.3 11.6 0 7.5 0Z" fill="#fff"/><circle cx="7.5" cy="7.4" r="2.8" fill="var(--gold-footer)"/></svg>
    <span>48, Kranji Loop Road,<br>Singapore 739560</span>
  </div>
  <div class="contact" style="left:451px">
    <svg width="18" height="18" viewBox="0 0 18 18"><path d="M4 1 L7 5 L5 7 Q7 11 11 13 L13 11 L17 14 L15 17 Q6 16 1 3 Z" fill="none" stroke="#fff" stroke-width="1.6"/><path d="M11 1 Q16 2 17 7 M11 4 Q14 5 14 7" stroke="#fff" stroke-width="1.4" fill="none"/></svg>
    <span>(+65) 9123 4567</span>
  </div>
  <div class="contact" style="left:623px">
    <svg width="18" height="14" viewBox="0 0 18 14"><rect x="1" y="1" width="16" height="12" fill="none" stroke="#fff" stroke-width="1.6"/><path d="M1 1 L9 8 L17 1" fill="none" stroke="#fff" stroke-width="1.6"/></svg>
    <span>sales@tanbokleong.com</span>
  </div>
  <div class="contact" style="left:623px;top:1142px">
    <svg width="18" height="18" viewBox="0 0 18 18" fill="none" stroke="#fff" stroke-width="1.4"><circle cx="9" cy="9" r="7.5"/><ellipse cx="9" cy="9" rx="3.3" ry="7.5"/><path d="M1.5 9 H16.5 M3 5 H15 M3 13 H15"/></svg>
    <span>www.tanbokleong.com</span>
  </div>
</main>
</body>
</html>
```